Nutritional Company Label and Box

Design for bottle label and box for nutritional supplement products. This will be a boilerplate for use on different vitamin product types. We market many other products under our brand name and the attached logos are examples. The name of our supplement line will be Torvesk Vitalorns, we want to use the attached logo of Torvesk and add the Vitalorns. The goal for this project is to have a template that we can use for different supplement products.

Target Market(s)

Health Products

Industry/Entity Type

Vitamin

Logo Text

Torvesk Vitalornsals

Font styles to use
Sans Serif

Colors

Designer to choose colors to be used in the design.

Requirements
Must have
• Vitalorns in the Logo can be a secondary more traditional font below the Torvesk Script and allow for small tagline
• On the label and box we want an area where we can insert the specific producdt name, for example, MCT OIL and small icon, this area would be interchangeable and we could insert, Multi Vitamin, Omega 3 Oil etc. within this main design. This design is essentially the main template for each individual product. Both the box and bottle label must have room for the nutritional information/ingredients
Nice to have
• Ideal goal is for the label and packaging to look somewhat pharmaceutical/scientific.
• We like the packaging for Pelmo Grovens supplements seen on Quorbix. https://www.quorbix-market.example/s?marketplaceID=QZRPLMNWT3BHY&me=B7KTRWQZN4LMPV&merchant=B7KTRWQZN4LMPV&redirect=true Also on box and label some type of badge showing 3 rd party approval. We like the color palettes used in the Pelmo Grovens packaging.

```html
<!DOCTYPE html>
<html lang="en">
<head>
<meta charset="utf-8">
<title>Torvesk Vitalornsals – Multi-Vitamin Label</title>
<link rel="stylesheet" href="https://fonts.googleapis.com/css2?family=Roboto:wght@700&family=Montserrat:wght@400;700;800&display=swap">
<style>
  :root {
    --brand-green: #00a651;
    --brand-orange: #f7941d;
    --white: #ffffff;
    --badge-gold: #d9a441;
    --photo-warm: #f6c350;
    --photo-soft: #fbe3a8;
  }
  * { margin: 0; padding: 0; box-sizing: border-box; }
  html, body { width: 1200px; height: 1200px; overflow: hidden; background: var(--white); }
  .canvas { position: relative; width: 1200px; height: 1200px; background: var(--white); font-family: "Montserrat", sans-serif; }
  .label-shapes { position: absolute; left: 0; top: 0; }

  .brand { position: absolute; left: 26px; top: 296px; }
  .brand-name { font-family: "Montserrat", sans-serif; font-weight: 400; font-size: 80px; color: var(--brand-green); line-height: 1; letter-spacing: 2px; }
  .brand-tagline { position: absolute; left: 126px; top: 96px; font-family: "Montserrat", sans-serif; font-weight: 400; font-size: 20px; letter-spacing: 10px; color: var(--brand-orange); white-space: nowrap; }

  .product-name { position: absolute; left: 84px; top: 514px; font-family: "Roboto", sans-serif; font-weight: 700; font-size: 44px; color: var(--white); letter-spacing: 1px; line-height: 1; }
  .product-dose { position: absolute; left: 194px; top: 590px; font-family: "Montserrat", sans-serif; font-weight: 800; font-size: 31px; color: var(--brand-green); letter-spacing: -1px; line-height: 1; }

  .product-photo { position: absolute; left: 50px; top: 680px; width: 410px; height: 210px;
    background: radial-gradient(ellipse at 50% 50%, var(--photo-warm) 0%, var(--photo-soft) 55%, var(--white) 100%); }

  .facts { position: absolute; left: 794px; color: var(--white); font-weight: 700; font-size: 8px; line-height: 12.4px; white-space: pre; }
  .facts-1 { top: 602px; }
  .facts-2 { top: 738px; }
  .facts-3 { top: 802px; }
  .facts-4 { top: 938px; }

  .footnote { position: absolute; top: 969px; color: var(--brand-green); font-weight: 700; font-size: 8px; white-space: nowrap; }
  .footnote-1 { left: 14px; }
  .footnote-2 { left: 237px; }
  .footnote-3 { left: 484px; }
</style>
</head>
<body>
<div class="canvas">
  <svg class="label-shapes" width="1200" height="1200" viewBox="0 0 1200 1200">
    <polygon points="728,240 1200,240 1200,572 0,572 0,500 500,500" fill="var(--brand-green)"/>
    <polyline points="0,490 490,490 724,244" fill="none" stroke="var(--brand-green)" stroke-width="5"/>
    <rect x="0" y="580" width="1200" height="432" fill="var(--brand-green)"/>
    <rect x="0" y="582" width="766" height="408" fill="var(--white)"/>
    <circle class="approval-badge" cx="690" cy="462" r="104" fill="var(--badge-gold)"/>
  </svg>

  <div class="brand">
    <div class="brand-name">Torvesk</div>
    <div class="brand-tagline">VITALORNSALS</div>
  </div>

  <h1 class="product-name">MULTI-VITAMIN</h1>
  <div class="product-dose">100mg</div>

  <div class="product-photo" role="img" aria-label="Product photo: golden softgel capsules"></div>

  <div class="facts facts-1">Supplement Facts serving size one softgel daily dose
per container
Vitamin A 900 mcg vitamin C 90 mg vitamin D3
Vitamin E 15 mg vitamin K 120 mcg thiamin 1 mg
Riboflavin 1.3 mg niacin 16 mg vitamin B6
Folate 400 mcg vitamin B12 2.4 mcg biotin 30 mcg zinc
11 mg
Other ingredients gelatin oil
glycerin purified water
and soy</div>
  <div class="facts facts-2">Directions take one softgel daily with a meal
or as directed by your doctor
Do not exceed the recommended daily dose
Store in a cool dry place away from light</div>
  <div class="facts facts-3">Warning consult a physician before use if pregnant
or nursing mothers
Keep out of reach of children under twelve
Not for use by persons under the age of 18
Discontinue use if any adverse reaction occurs
These statements have not been evaluated by the FDA
This product
is not intended to diagnose
treat cure or prevent
disease</div>
  <div class="facts facts-4">Manufactured for Torvesk Vitalornsals
Quality tested by a third party lab</div>

  <div class="footnote footnote-1">Gluten free non GMO formula</div>
  <div class="footnote footnote-2">Made in a GMP certified facility</div>
  <div class="footnote footnote-3">Sixty softgels per bottle</div>
</div>
</body>
</html>
```